Website to promote New Zealand as a destination by QRM

We are a company that promotes New Zealand education, migration, business and travel opportunities. We want a website to reflect all these activities. We have an existing website that should be used as a base template and add the other required pages to it. The current website is what we want to expand upon. Access to the files of the current website may not be possible since the previous designer cannot be contacted. So the new designer has to use the existing template and build the whole thing from there. It should be an easy job since there is already a clear sample of what we want. I would like the same flow to continue where the impact is very high visually and very little text content. I expect most clients to use a mobile device to access the site. so it has to be extremely mobile friendly.
Updates

Target Market(s)

Anybody between ages of 16-60 who would like to study, settle, work, travel or invest in New Zealand.

Industry/Entity Type

Education

Contact Information for Business Card

Tomas Velik
Licensed Immigration Adviser
License No 307214958

Mob: +64 239187045
Email: tomas.velik@qrm-example.kiwi
QRM Services Limited
4417 Ferncliff Lane
Ashbury
Hamilton
New Zealand - 3210

www.qrm-example.kiwi

Coding

Coded - Design and coding required

Number of Pages Required

5+ page

Font styles to use
Sans Serif

Requirements
Must have
• MUST use the existing design of our website and build other pages from it.
Should not have
• Nil

```html
<!DOCTYPE html>
<html lang="en">
<head>
<meta charset="utf-8">
<title>QRM Group – Our Services</title>
<link href="https://fonts.googleapis.com/css2?family=Roboto:wght@300;400;500&family=Lato:wght@400;700&family=Cousine&display=swap" rel="stylesheet">
<style>
:root{
  --header-bg:#454545;
  --footer-bg:#232323;
  --heading:#444444;
  --body-text:#666666;
  --accent:#6b1f9e;
  --icon:#7b2fb3;
  --white:#ffffff;
  --button:#f2195a;
  --field-bg:rgba(55,30,110,.55);
  --field-border:rgba(110,80,190,.7);
}
*{box-sizing:border-box;margin:0;padding:0}
html,body{width:1135px;height:1200px;overflow:hidden;background:var(--white)}
body{position:relative;font-family:'Roboto',sans-serif}

.site-header{position:absolute;left:0;top:0;width:1135px;height:53px;background:var(--header-bg)}
.brand{position:absolute;left:132px;top:14px;display:flex;align-items:center;gap:6px;color:var(--white);font-family:'Roboto',sans-serif;font-weight:500;font-size:18px;letter-spacing:.5px}
.brand-dot{width:24px;height:24px;border-radius:50%;border:2px solid var(--white)}
.main-nav{position:absolute;top:19px;font-size:12.5px;font-weight:500;color:var(--white);letter-spacing:.2px;white-space:nowrap}
.main-nav span{position:absolute;top:0}
.caret{font-size:9px;margin-left:3px}

.services-title{position:absolute;left:0;width:1135px;top:96px;text-align:center;font-size:32px;font-weight:500;color:var(--heading)}
.services-intro{position:absolute;left:170px;width:795px;top:144px;text-align:center;font-size:11px;line-height:19.5px;font-weight:300;color:var(--body-text)}

.service{position:absolute;width:290px;text-align:center}
.service svg{display:block;margin:0 auto;width:64px;height:58px}
.service h3{margin-top:14px;font-size:20px;font-weight:400;color:var(--heading);letter-spacing:.3px}
.service p{margin-top:10px;font-size:11px;line-height:19.5px;font-weight:300;color:var(--body-text)}
.service .more{display:block;margin-top:14px;font-size:11px;color:var(--accent);text-decoration:none}
.service .shadow{margin:14px auto 0;width:235px;height:5px;border-radius:50%;background:radial-gradient(ellipse at center,rgba(0,0,0,.45) 0%,rgba(0,0,0,0) 70%)}

.contact{position:absolute;left:0;top:742px;width:1135px;height:408px;background:linear-gradient(100deg,#7a1f3a 0%,#4b2a6e 25%,#7a2a7a 50%,#5a1548 75%,#2a0e24 100%)}
.contact-title{position:absolute;left:0;width:1135px;top:28px;text-align:center;font-family:'Lato',sans-serif;font-size:44px;font-weight:400;color:var(--white)}
.field{position:absolute;background:var(--field-bg);border:1px solid var(--field-border);color:rgba(255,255,255,.75);font-size:13px;padding:0 10px;display:flex;align-items:center}
.field.area{align-items:flex-start;padding-top:8px;font-family:'Cousine',monospace;font-size:12px}
.enquire{position:absolute;left:378px;top:303px;width:132px;height:37px;background:var(--button);color:var(--white);font-size:14px;display:flex;align-items:center;justify-content:center;border-radius:2px}
.office{position:absolute;left:823px;top:130px;color:var(--white);font-family:'Lato',sans-serif}
.office h4{font-size:20px;font-weight:700;margin-bottom:6px}
.office p{font-size:13px;line-height:22px;font-weight:400}
.social{display:flex;gap:7px;margin-top:10px}
.social span{width:32px;height:32px;border-radius:50%;background:var(--white)}

.site-footer{position:absolute;left:0;top:1150px;width:1135px;height:50px;background:var(--footer-bg);color:var(--white);font-size:11px}
.site-footer .copy{position:absolute;left:0;width:1135px;top:18px;text-align:center}
.site-footer .code{position:absolute;left:1044px;top:18px}
</style>
</head>
<body>

<header class="site-header">
  <div class="brand"><span class="brand-dot"></span>QRM GROUP</div>
  <nav class="main-nav">
    <span style="left:569px">HOME<span class="caret">»</span></span>
    <span style="left:651px">MIGRATION SERVICES<span class="caret">»</span></span>
    <span style="left:822px">INFOTECH SERVICES<span class="caret">»</span></span>
    <span style="left:986px">CONTACT</span>
  </nav>
</header>

<h1 class="services-title">OUR SERVICES</h1>
<p class="services-intro">QRM group is a New Zealand based business house with current interests in migration and information technology. Success through simplicity is the credo that underpins all our products and services for the benefit of our customers, employees, shareholders and community.</p>

<div class="service" style="left:89px;top:218px">
  <svg viewBox="0 0 64 58" fill="none" stroke="var(--icon)" stroke-width="1.4"><path d="M2 18 L34 4 L62 16 L32 28 Z"/><path d="M14 22 V36 C22 44 44 44 50 36 V22"/><path d="M10 20 V40"/><rect x="7" y="40" width="6" height="14"/></svg>
  <h3>EDUCATION</h3>
  <p>There are many variations of passages of Lorem Ipsum available, but the majority have suffered alteration in some form, by injected humour, or randomised</p>
  <a class="more">MORE</a><div class="shadow"></div>
</div>

<div class="service" style="left:423px;top:218px">
  <svg viewBox="0 0 64 58" fill="none" stroke="var(--icon)" stroke-width="1.4"><path d="M10 24 A22 22 0 0 1 52 18"/><path d="M54 34 A22 22 0 0 1 12 40"/><path d="M46 14 L53 18 L55 10"/><path d="M18 44 L11 40 L9 48"/><circle cx="32" cy="29" r="9"/><circle cx="32" cy="29" r="3.5"/></svg>
  <h3>MIGRATION</h3>
  <p>There are many variations of passages of Lorem Ipsum available, but the majority have suffered alteration in some form, by injected humour, or randomised</p>
  <a class="more">MORE</a><div class="shadow"></div>
</div>

<div class="service" style="left:758px;top:218px">
  <svg viewBox="0 0 64 58" fill="none" stroke="var(--icon)" stroke-width="1.4"><circle cx="32" cy="29" r="20" stroke-dasharray="6 3"/><circle cx="32" cy="29" r="13"/><path d="M26 22 L44 44 L48 40 L30 18"/><circle cx="25" cy="21" r="4"/></svg>
  <h3>WORK</h3>
  <p>There are many variations of passages of Lorem Ipsum available, but the majority have suffered alteration in some form, by injected humour, or randomised</p>
  <a class="more">MORE</a><div class="shadow"></div>
</div>

<div class="service" style="left:255px;top:480px">
  <svg viewBox="0 0 64 58" fill="none" stroke="var(--icon)" stroke-width="1.4"><rect x="4" y="14" width="56" height="40" rx="3"/><path d="M22 14 V6 H42 V14"/><path d="M4 30 H60"/><rect x="26" y="25" width="12" height="10" rx="3"/></svg>
  <h3>BUSINESS</h3>
  <p>There are many variations of passages of Lorem Ipsum available, but the majority have suffered alteration in some form, by injected humour, or randomised</p>
  <a class="more">MORE</a><div class="shadow"></div>
</div>

<div class="service" style="left:590px;top:480px">
  <svg viewBox="0 0 64 58" fill="none" stroke="var(--icon)" stroke-width="1.4"><circle cx="24" cy="34" r="21"/><path d="M8 28 C16 30 18 38 24 40 C28 46 22 52 24 54"/><path d="M46 30 C36 22 34 14 40 6 C46 0 58 2 60 12 C62 20 52 26 46 30 Z"/><circle cx="48" cy="13" r="4"/></svg>
  <h3>TRAVEL</h3>
  <p>There are many variations of passages of Lorem Ipsum available, but the majority have suffered alteration in some form, by injected humour, or randomised</p>
  <a class="more">MORE</a><div class="shadow"></div>
</div>

<section class="contact" role="img" aria-label="Abstract purple and crimson geometric background">
  <h2 class="contact-title">CONTACT US</h2>
  <div class="field" style="left:130px;top:130px;width:302px;height:36px">Name</div>
  <div class="field" style="left:130px;top:187px;width:302px;height:36px">Email</div>
  <div class="field" style="left:130px;top:244px;width:302px;height:36px">Phone</div>
  <div class="field area" style="left:452px;top:130px;width:303px;height:150px">Text</div>
  <div class="enquire">ENQUIRE</div>
  <address class="office" style="font-style:normal">
    <h4>QRM Group</h4>
    <p>PO Box 58231,<br>Ferncliff Post Shop,<br>Hamilton, Waikato,<br>New Zealand<br>Email: info@qrm-example.kiwi</p>
    <div class="social"><span></span><span></span><span></span><span></span></div>
  </address>
</section>

<footer class="site-footer">
  <div class="copy">© - 2016 QRM Group | Privacy Policy | All rights reserved.</div>
  <div class="code">C 19</div>
</footer>

</body>
</html>
```